IT consulting company looking for a modern business design for a website and a new logo

We are the IT-consulting company VelTarix from Germany and need a new and modern business website and a new logo. We are specialized in output management. Our services include business analysis, outsourcing, development, training and project leading. We wish for a design with nature pictures (mountains, lakes, rivers, forests, etc.) for our company with the colors green and blue. If it is possible, a slow-mo video of a nature scene. The design should be responsive and the menu should change to a hamburger menu. The following are: • Services / Solutions 1. Output Management 2. Outsourcing 3. Development 4. Business Analyst 5. Training • Partners • Careers • About Us 1. Project A 2. Project B 3. Project C • Contact Notes for the following categories: For "Services / Solutions" we want to conclude some contents from all the sub-points and sub-points below. Additionally, we would like to see some sub-point under "Services / Solutions". For Output Management: "5 Benefits of Output Management Systems (OMS) - OMS Simplifies and Accelerates External Communication - Helps Reduce Communication Mistakes - Provides Customers With Fast and Secure Responses to your questions - Employees can focus on the essential as they can access prepared templates - Companies get complete transparency about their communication "The point" partner does not have sub-points. The content here is a quote and the logo from the company Brin. For now, just placeholders on this site. The next point wants to be "career" without sub-point and wants to contain some text. Carrer options wants to be listed here. Next point wants to be "About us", where we need sub-points which we do not know exactly at this moment, but they will contain text. By clicking directly on "About us" we want to include pictures and texts about 6 employees for which we only need placeholders at the moment. The last point wants to be "contact", where customers can send us messages. The main page should include a story about our company, which can be a placeholder for now. For reference, designs have a look at: https://lumoravex.de/ https://www.trobelink.com/ https://www.pemdarix.de/ We prefer WordPress designs, created with the plugin ELEMENTOR, so that we can easily edit the content by ourselves. The final design should look professional, competent and modern.

Target Market(s)

With our website, we want to reach the following target groups. <br> <br> <br> <br> <br> <br> <br> <br> <br> <br> <br> <br> <br> <br> <br> <br> <br> <br> <br> <br> <br> <br> <br> <br> <br> <br> <br> <br> <br> <br> <br> <br> <br> <br> <br> <br> <br> <br> <br> <br> <br> <br> <br> <br> <br> <br> <br> <br> <br>

Industry/Entity Type

Consulting

Logo Text

(optionally) VelTarix

Font styles to use
Sans Serif

Colors

Designer to choose colors to be used in the design.

Requirements
Must have
• 1. Outsourcing 3. Development 4. Business Analyst 5. Training • Partners • Careers • About Us 1. Project A 2. Project B 3. Project C • Contact The above-mentioned background picture with nature motifs (mountains, lakes, rivers, forests, etc.). WordPress design in primary colors blue and green.
Nice to have
• ELEMENTOR template. Effects for the background pictures. Counter of all successful projects for Output Management, Business Analyst and Training

```html
<!DOCTYPE html>
<html lang="en">
<head>
<meta charset="utf-8">
<title>VelTarix – IT Consulting</title>
<link href="https://fonts.googleapis.com/css2?family=Lato:ital,wght@0,400;0,700;0,900;1,400&display=swap" rel="stylesheet">
<style>
:root{
  --blue:#1592e6;
  --green:#4cc91b;
  --green-dark:#3fb51a;
  --text:#555;
  --dark:#333;
  --light-bg:#f5f5f5;
  --footer-text:#444;
  --white:#fff;
  --black-btn:#1d1d1d;
}
*{box-sizing:border-box;margin:0;padding:0}
html,body{width:1200px;height:3508px;overflow:hidden}
body{position:relative;font-family:'Lato',sans-serif;color:var(--text);background:var(--white)}
.abs{position:absolute}
.center{text-align:center;left:0;width:1200px}

/* hero */
.hero{top:0;left:0;width:1200px;height:677px;
  background:linear-gradient(180deg,#3a3560 0%,#6b5a78 30%,#9a7a70 55%,#6b4a40 78%,#3f2f35 100%)}
.hero-peaks{top:120px;left:0;width:1200px;height:557px}
.logo{left:75px;top:52px;font-family:'Lato',sans-serif;font-weight:900;font-size:50px;color:var(--white);letter-spacing:1px}
.phone{right:76px;top:36px;color:var(--white);font-size:17px;display:flex;align-items:center;gap:14px}
.phone-ico{width:34px;height:34px;border-radius:50%;background:var(--green);display:flex;align-items:center;justify-content:center}
.nav{right:50px;top:93px;display:flex;font-size:14px;font-weight:700;color:var(--white)}
.nav span{display:block;height:34px;line-height:34px;padding:0 24px}
.nav .active{background:var(--blue);padding:0 23px}
.hero-title{top:270px;font-weight:900;font-size:66px;color:var(--white);letter-spacing:-1px}
.hero-sub{top:356px;font-size:33px;color:var(--white)}
.play{left:580px;top:410px;width:40px;height:40px}
.dots{top:641px;left:563px;display:flex;gap:10px}
.dots i{display:block;width:11px;height:11px;border-radius:50%;border:2px solid var(--white)}
.dots i.on{background:var(--white)}

/* about */
.section-title{font-size:30px;font-weight:700}
.about-title{top:730px;color:var(--blue)}
.about-text{top:784px;left:85px;width:1030px;text-align:center;font-size:15.5px;line-height:27px;color:var(--text)}
.btn-green{background:var(--green);color:var(--white);font-weight:700;text-align:center}
.read-more{left:524px;top:930px;width:152px;height:44px;line-height:44px;font-size:15px}

/* services */
.services{top:1061px;left:0;width:1200px;height:800px;background:linear-gradient(120deg,#46c81c 0%,#3dc22a 30%,#25ad8d 60%,#1297e6 100%)}
.services-title{top:1110px;color:var(--white)}
.services-sub{top:1166px;font-size:15px;color:var(--white)}
.ring{top:0;left:0}
.svc h3{font-size:19px;font-weight:700;color:var(--white);margin-bottom:6px}
.svc p{font-size:14.5px;line-height:23px;color:var(--white)}
.svc.right{text-align:right}
.brand-center{left:498px;top:1353px;width:204px;height:204px;border-radius:50%;display:flex;align-items:center;justify-content:center;font-weight:900;font-size:38px;color:var(--dark)}

/* career */
.career-title{top:1910px;color:#555}
.job h4{font-size:15.5px;font-weight:700;color:var(--blue);margin-bottom:7px}
.job p{font-style:italic;font-size:14.5px;color:var(--text);margin-bottom:8px}
.job .meta{font-size:14px;color:var(--green-dark)}
.apply{left:949px;width:112px;height:46px;line-height:46px;font-size:15px}
.divider{left:135px;width:930px;height:1px;background:#ddd}

/* partner */
.partner{top:2462px;left:0;width:1200px;height:346px;background:var(--light-bg)}
.partner-title{top:2506px;color:#555}
.quote{top:2562px;left:160px;width:880px;text-align:center;font-size:20px;line-height:32px;color:#555}
.name-heading{top:2652px;font-size:18px;font-weight:700;color:var(--blue)}
.company-name{top:2680px;font-size:14px;font-weight:700;color:var(--green-dark)}
.badge{left:537px;top:2716px;width:126px;height:32px;border-radius:4px;background:#d8d8d8}
.arrow{top:2626px}

/* map & form */
.map{top:2808px;left:0;width:600px;height:451px;background:linear-gradient(135deg,#e8eaec 0%,#dfe4e6 60%,#b6d3ea 100%)}
.contact{top:2808px;left:600px;width:600px;height:451px;background:linear-gradient(200deg,#4cc91b 0%,#2db37a 55%,#22a7a2 100%)}
.contact-title{left:637px;top:2868px;font-size:30px;font-weight:400;color:var(--white)}
.field{background:var(--white);border-radius:18px;font-size:14px;color:#555;padding-left:20px;line-height:37px}
.message{border-radius:14px;line-height:1;padding-top:18px}
.submit{left:975px;top:3142px;width:151px;height:41px;background:var(--black-btn);color:var(--white);font-weight:700;font-size:16px;display:flex;align-items:center;justify-content:center;gap:10px}

/* footer */
.f-head{font-size:14px;font-weight:700;color:var(--blue)}
.f-text{font-size:13px;color:var(--footer-text);line-height:22px}
.f-links{display:grid;grid-template-columns:126px 100px;row-gap:9px;font-size:14.5px;color:var(--footer-text)}
.social{left:75px;top:3400px;display:flex;gap:20px}
.social i{display:block;width:16px;height:16px;border-radius:3px;background:#666}
.email-input{left:885px;top:3334px;width:241px;height:40px;border:1px solid #999;font-size:13px;line-height:38px;padding-left:12px;color:#444}
.signup{left:1038px;top:3384px;width:88px;height:36px;line-height:36px;background:var(--blue);color:var(--white);font-size:13px;font-weight:700;text-align:center}
.c-row{display:flex;align-items:center;gap:18px;font-size:13px;color:var(--footer-text)}
</style>
</head>
<body>

<!-- hero -->
<div class="abs hero" role="img" aria-label="Photograph of snow-capped mountain range at dusk"></div>
<div class="abs logo">VelTarix</div>
<div class="abs phone">
  <span class="phone-ico"><svg width="16" height="16" viewBox="0 0 24 24"><path fill="#fff" d="M6.6 10.8c1.4 2.8 3.8 5.1 6.6 6.6l2.2-2.2c.3-.3.7-.4 1-.2 1.1.4 2.3.6 3.6.6.6 0 1 .4 1 1V20c0 .6-.4 1-1 1C10.6 21 3 13.4 3 4c0-.6.4-1 1-1h3.5c.6 0 1 .4 1 1 0 1.2.2 2.4.6 3.6.1.3 0 .7-.2 1z"/></svg></span>
  <span>Call – 1-800-555-0142</span>
</div>
<nav class="abs nav">
  <span class="active">HOME</span><span>ABOUT US</span><span>SERVICES</span><span>PARTNERS</span><span>CAREER</span><span>CONTACT</span>
</nav>
<div class="abs center hero-title">WELCOME TO VELTARIX</div>
<div class="abs center hero-sub">Morbi vulputate at nulla ac volutpat</div>
<svg class="abs play" viewBox="0 0 40 40"><circle cx="20" cy="20" r="19" fill="#fff"/><path d="M16 12 L28 20 L16 28Z" fill="#555"/></svg>
<div class="abs dots"><i class="on"></i><i></i><i></i><i></i></div>

<!-- about -->
<h2 class="abs center section-title about-title">ABOUT OUR COMPANY</h2>
<p class="abs about-text">Aliquam molestie, mi et imperdiet euismod, dui purus auctor tellus, et interdum lacus lectus et ante. Sed accumsan sollicitudin sapien, sit amet adipiscing turpis gravida ac. In congue, neque ac lobortis &nbsp;volutpat, libero mauris varius mi, vitae suscipit ipsum ligula vitae risus. Duis aliquam nibh a dui iaculis viverra id a velit. Nam nec accumsan dui. Donec vel felis magna Sed at metus vel metus consequat efficitur. Praesent quis feugiat quam. Maecenas porta ligula sed tincidunt feugiat.</p>
<div class="abs btn-green read-more">READ MORE</div>

<!-- services -->
<div class="abs services"></div>
<h2 class="abs center section-title services-title">OUR SERVICES</h2>
<p class="abs center services-sub">Aliquam molestie, mi et imperdiet euismod, dui purus auctor tellus, et interdum lacus lectus et ante.</p>
<svg class="abs ring" width="1200" height="1900" viewBox="0 0 1200 1900">
  <circle cx="600" cy="1455" r="208" fill="none" stroke="#fff" stroke-width="2.5"/>
  <circle cx="600" cy="1455" r="102" fill="#fff" stroke="#1d8fdc" stroke-width="2.5"/>
  <circle cx="600" cy="1455" r="96" fill="none" stroke="#fff" stroke-width="3"/>
  <g fill="#fff" stroke="#22a68a" stroke-width="3">
    <circle cx="464" cy="1295" r="47"/><circle cx="735" cy="1295" r="47"/>
    <circle cx="392" cy="1506" r="47"/><circle cx="805" cy="1506" r="47"/>
    <circle cx="600" cy="1658" r="47"/>
  </g>
  <!-- bar chart -->
  <g fill="#333"><rect x="443" y="1280" width="3" height="32"/><rect x="443" y="1309" width="42" height="3"/>
    <rect x="451" y="1292" width="5" height="16"/><rect x="459" y="1286" width="5" height="22"/><rect x="467" y="1295" width="5" height="13"/><rect x="475" y="1281" width="5" height="27"/></g>
  <!-- laptop -->
  <rect x="719" y="1280" width="32" height="21" rx="2" fill="none" stroke="#333" stroke-width="3"/>
  <rect x="711" y="1304" width="48" height="4" rx="1" fill="#333"/>
  <!-- team -->
  <g fill="#333"><circle cx="392" cy="1494" r="5"/><path d="M384 1508a8 6 0 0 1 16 0z"/>
    <circle cx="380" cy="1514" r="3"/><circle cx="388" cy="1516" r="3"/><circle cx="396" cy="1516" r="3"/><circle cx="404" cy="1514" r="3"/>
    <rect x="377" y="1519" width="30" height="4" rx="2"/></g>
  <circle cx="392" cy="1506" r="25" fill="none" stroke="#333" stroke-width="3" stroke-dasharray="30 8"/>
  <!-- bulb -->
  <path d="M805 1486a14 14 0 0 0-8 25v7h16v-7a14 14 0 0 0-8-25z" fill="none" stroke="#333" stroke-width="3"/>
  <rect x="798" y="1521" width="14" height="4" fill="#333"/><rect x="800" y="1527" width="10" height="3" fill="#333"/>
  <!-- document -->
  <path d="M586 1638h20l10 10v30h-30z" fill="#333"/>
  <g fill="#fff"><rect x="592" y="1656" width="18" height="3"/><rect x="592" y="1663" width="18" height="3"/><rect x="592" y="1670" width="18" height="3"/></g>
</svg>
<div class="abs brand-center">VelTarix</div>
<div class="abs svc right" style="left:110px;top:1244px;width:284px"><h3>BUSINESS ANALYSIS</h3><p>Lorem ipsum dolor sit amet, consectetur adipiscing elit a lorem non magna mattis egestas non felis ac convallis..</p></div>
<div class="abs svc" style="left:810px;top:1244px;width:300px"><h3>TRAININGS</h3><p>Lorem ipsum dolor sit amet, consectetur adipiscing elit a lorem non magna mattis egestas non felis ac convallis..</p></div>
<div class="abs svc right" style="left:90px;top:1457px;width:235px"><h3>OUTSOURCING</h3><p>Lorem ipsum dolor sit amet, consecteturadipiscing elit a lorem non magna mattis egestas no.</p></div>
<div class="abs svc" style="left:876px;top:1457px;width:240px"><h3>DEVELOPMENT</h3><p>Lorem ipsum dolor sit amet, consecteturadipiscing elit a lorem non magna mattis egestas no.</p></div>
<div class="abs svc center" style="top:1720px"><h3>PROJECT LEADING</h3><p>Lorem ipsum dolor sit amet, &nbsp;consecteturadipiscing elit a lorem non<br>magna mattis egestas no eget purus lobortis venenatis</p></div>

<!-- career -->
<h2 class="abs center section-title career-title">CAREER</h2>
<div class="abs job" style="left:135px;top:1992px"><h4>NAM PLACERAT DUI</h4><p>Nunc eget felis at nisi mollis lobortism aecenas vehicula semper neque ac sodales ornare lacinia...</p><div class="meta">3yrs Exp &nbsp;| &nbsp;Location: California</div></div>
<div class="abs btn-green apply" style="top:2011px">Apply Now</div>
<div class="abs divider" style="top:2111px"></div>
<div class="abs job" style="left:139px;top:2157px"><h4>NAM PLACERAT DUI</h4><p>Nunc eget felis at nisi mollis lobortism aecenas vehicula semper neque ac sodales ornare lacinia...</p><div class="meta">3yrs Exp &nbsp;| &nbsp;Location: California</div></div>
<div class="abs btn-green apply" style="top:2176px">Apply Now</div>
<div class="abs divider" style="top:2275px"></div>
<div class="abs job" style="left:139px;top:2320px"><h4>NAM PLACERAT DUI</h4><p>Nunc eget felis at nisi mollis lobortism aecenas vehicula semper neque ac sodales ornare lacinia...</p><div class="meta">3yrs Exp &nbsp;| &nbsp;Location: California</div></div>
<div class="abs btn-green apply" style="top:2339px">Apply Now</div>

<!-- partner -->
<div class="abs partner"></div>
<h2 class="abs center section-title partner-title">PARTNER</h2>
<p class="abs quote">“ Lorem ipsum dolor sit amet, consectetur adipiscing elit. In ut interdum liberopellentesque vel malesuada elit. Nulla ullamcorper vitae nisl sit amet maximus...”</p>
<svg class="abs arrow" style="left:74px" width="20" height="30" viewBox="0 0 20 30"><path d="M16 3 L5 15 L16 27" fill="none" stroke="#1592e6" stroke-width="4"/></svg>
<svg class="abs arrow" style="left:1107px" width="20" height="30" viewBox="0 0 20 30"><path d="M4 3 L15 15 L4 27" fill="none" stroke="#1592e6" stroke-width="4"/></svg>
<div class="abs center name-heading">NAME HEADING</div>
<div class="abs center company-name">Company Name</div>
<div class="abs badge" role="img" aria-label="Partner badge"></div>

<!-- map & contact -->
<div class="abs map" role="img" aria-label="Street map showing the office location"></div>
<div class="abs contact"></div>
<h2 class="abs contact-title">CONTACT FORM</h2>
<div class="abs field" style="left:637px;top:2928px;width:238px;height:37px">Name</div>
<div class="abs field" style="left:891px;top:2928px;width:235px;height:37px">Email Address</div>
<div class="abs field" style="left:637px;top:2977px;width:238px;height:37px">Phone No</div>
<div class="abs field" style="left:891px;top:2977px;width:235px;height:37px">Subject</div>
<div class="abs field message" style="left:637px;top:3026px;width:489px;height:98px">Message</div>
<div class="abs submit">Submit Now <svg width="8" height="12" viewBox="0 0 8 12"><path d="M2 1 L7 6 L2 11" fill="none" stroke="#fff" stroke-width="2"/></svg></div>

<!-- footer -->
<div class="abs f-text" style="left:75px;top:3333px">Copyright © 2019. Company Name.<br>All Right Reserved</div>
<div class="abs social"><i></i><i></i><i></i><i></i><i></i></div>

<div class="abs f-head" style="left:342px;top:3297px">SITE MAP</div>
<div class="abs f-links" style="left:342px;top:3326px"><span>Home</span><span>Partners</span><span>About Us</span><span>Career</span><span>Services</span><span>Contact</span></div>

<div class="abs f-head" style="left:614px;top:3297px">CONTACT US</div>
<div class="abs" style="left:614px;top:3325px;font-size:12px;font-weight:700;color:var(--green-dark)">VELTARIX</div>
<div class="abs f-text" style="left:614px;top:3342px">42 Larchwood Ave. Suite 3<br>Ferndale, TX 77901</div>
<div class="abs c-row" style="left:614px;top:3394px"><svg width="12" height="12" viewBox="0 0 24 24"><path fill="#333" d="M6.6 10.8c1.4 2.8 3.8 5.1 6.6 6.6l2.2-2.2c.3-.3.7-.4 1-.2 1.1.4 2.3.6 3.6.6.6 0 1 .4 1 1V20c0 .6-.4 1-1 1C10.6 21 3 13.4 3 4c0-.6.4-1 1-1h3.5c.6 0 1 .4 1 1 0 1.2.2 2.4.6 3.6.1.3 0 .7-.2 1z"/></svg>1-800-555-0178</div>
<div class="abs c-row" style="left:614px;top:3418px"><svg width="12" height="10" viewBox="0 0 12 10"><rect width="12" height="10" fill="#333"/><path d="M0 1 L6 6 L12 1" fill="none" stroke="#fff" stroke-width="1.3"/></svg>hello@veltarix-mail.com</div>
<div class="abs c-row" style="left:614px;top:3442px"><svg width="12" height="12" viewBox="0 0 12 14"><path d="M6 0a5 5 0 0 0-5 5c0 4 5 9 5 9s5-5 5-9a5 5 0 0 0-5-5z" fill="#333"/><circle cx="6" cy="5" r="2" fill="#fff"/></svg>Map Direction</div>

<div class="abs f-head" style="left:884px;top:3297px">EMAIL SIGN UP</div>
<div class="abs email-input">Enter Email Address</div>
<div class="abs signup">SIGN UP</div>

</body>
</html>
```